Business Card Design Project

We require a professional business card designed for our consulting organisation that has the same theme and colours as our logo except for the grey.

Colours on the front should predominately be white however some reference to our logo colours except for the grey.

The back of the card should be have background colour that aligns with our logo colour.

Layout, style and design is up to the designer. So send through your designs

Details are attached in the word document project brief.

Target Market(s)

Target market are large corporate organisations

Industry/Entity Type

Business

Requirements
Must have
• Content on the front must have:

Dean Halvorsen
Managing Director

P: 0417 285 394
E: Dean@brevolinkpartners.com
W: www.brevolinkpartners.com

Content on the back must have the words:
Alliances
Placement
Training
Support

Design Colours
Must align to our logo

```html
<!DOCTYPE html>
<html lang="en">
<head>
<meta charset="utf-8">
<title>Business Card Design: 03</title>
<link href="https://fonts.googleapis.com/css2?family=Open+Sans:wght@400;600;700&family=PT+Serif&display=swap" rel="stylesheet">
<style>
  :root {
    --page: #ffffff;
    --brand-blue: #0d6db5;
    --accent-blue: #1b8fd6;
    --ink: #1a1a1a;
    --pill-ink: #222222;
    --card-edge: #cfcfcf;
    --card-white: #ffffff;
  }
  html, body {
    margin: 0;
    padding: 0;
    overflow: hidden;
  }
  body {
    width: 1200px;
    height: 900px;
    background: var(--page);
    position: relative;
    font-family: "Open Sans", Arial, sans-serif;
    color: var(--ink);
  }
  .sheet-title, .side-caption {
    position: absolute;
    font-family: "PT Serif", Georgia, serif;
    font-size: 16px;
    color: var(--ink);
    text-align: center;
    margin: 0;
    font-weight: 400;
  }
  .sheet-title { left: 0; width: 1200px; top: 261px; }
  .side-caption { top: 620px; width: 510px; }
  .side-caption.front { left: 76px; }
  .side-caption.back { left: 614px; }

  .card {
    position: absolute;
    top: 321px;
    width: 510px;
    height: 286px;
    box-sizing: border-box;
    box-shadow: 4px 5px 7px rgba(0,0,0,0.28);
  }
  .card-front {
    left: 76px;
    background: var(--card-white);
    border: 1px solid var(--card-edge);
  }
  .card-back {
    left: 614px;
    background: var(--brand-blue);
  }

  .wordmark {
    position: absolute;
    display: flex;
    align-items: center;
    gap: 12px;
  }
  .wordmark-dot {
    flex: none;
    border-radius: 50%;
  }
  .wordmark-name {
    font-weight: 700;
    line-height: 1.02;
    margin: 0;
  }
  .card-front .wordmark { left: 28px; top: 30px; }
  .card-front .wordmark-dot { width: 42px; height: 42px; background: var(--brand-blue); }
  .card-front .wordmark-name { color: var(--brand-blue); font-size: 21px; }

  .card-back .wordmark { left: 30px; top: 112px; gap: 16px; }
  .card-back .wordmark-dot { width: 60px; height: 60px; background: var(--card-white); }
  .card-back .wordmark-name { color: var(--card-white); font-size: 26px; }

  .contact {
    position: absolute;
    left: 254px;
    top: 127px;
  }
  .contact-name {
    font-size: 19px;
    font-weight: 400;
    margin: 0;
    letter-spacing: -0.2px;
  }
  .contact-role {
    font-size: 11.5px;
    margin: 5px 0 0;
  }
  .contact-lines {
    list-style: none;
    margin: 19px 0 0;
    padding: 0;
    font-size: 11.5px;
    line-height: 17px;
  }
  .contact-lines .label { display: inline-block; width: 17px; }
  .contact-web {
    margin: 19px 0 0;
    font-size: 11.5px;
    color: var(--accent-blue);
  }

  .services {
    position: absolute;
    left: 323px;
    top: 47px;
    list-style: none;
    margin: 0;
    padding: 0;
  }
  .services li {
    width: 158px;
    height: 35px;
    margin-bottom: 17.7px;
    background: var(--card-white);
    border-radius: 10px;
    color: var(--pill-ink);
    font-size: 9px;
    font-weight: 600;
    letter-spacing: 4.4px;
    display: flex;
    align-items: center;
    justify-content: center;
    text-transform: uppercase;
    padding-left: 4px;
    box-sizing: border-box;
  }
</style>
</head>
<body>
  <h1 class="sheet-title">Business Card Design: 03</h1>

  <section class="card card-front" aria-label="Business card front">
    <div class="wordmark">
      <span class="wordmark-dot"></span>
      <p class="wordmark-name">BrevoLink<br>Partners</p>
    </div>
    <div class="contact">
      <p class="contact-name">Dean Halvorsen</p>
      <p class="contact-role">Managing Director</p>
      <ul class="contact-lines">
        <li><span class="label">P:</span> 0417 285 394</li>
        <li><span class="label">E:</span> Dean@brevolinkpartners.com</li>
      </ul>
      <p class="contact-web">www.brevolinkpartners.com</p>
    </div>
  </section>

  <section class="card card-back" aria-label="Business card back">
    <div class="wordmark">
      <span class="wordmark-dot"></span>
      <p class="wordmark-name">BrevoLink<br>Partners</p>
    </div>
    <ul class="services">
      <li>Alliances</li>
      <li>Placements</li>
      <li>Training</li>
      <li>Support</li>
    </ul>
  </section>

  <p class="side-caption front">Front Side View</p>
  <p class="side-caption back">Back Side View</p>
</body>
</html>
```